Business Card Design - Pediatric Dentist

We need a business card for a new dental office. We are a pediatric dentist in Austin Tx. I would like a design that use bright green and if possible light blue.

Target Market(s)

Marketed to young moms

Industry/Entity Type

Dental

Contact Information for Business Card

Marcus Hollin DDS
Tidewell Pediatric Dentistry
438 E. Corvell Lane. Austin TX 78731
(512) 284 9153.

In the back i would like to state "we take most insurances, Chip & Medicaid" & a map

Colors
add136
cadf82
85cae6

```html
<!DOCTYPE html>
<html lang="en">
<head>
<meta charset="utf-8">
<title>Tidewell Pediatric Dentistry – Business Card</title>
<link rel="stylesheet" href="https://fonts.googleapis.com/css2?family=Tinos&family=Didact+Gothic&display=swap">
<style>
  :root {
    --card-bg: #f1fbec;
    --brand-green: #66e83a;
    --label-green: #7fe84c;
    --sky-blue: #85e6f3;
    --star-green: #6fdc3a;
    --tooth-white: #ffffff;
    --tooth-blue: #cfeaf7;
  }
  html, body {
    margin: 0;
    padding: 0;
    width: 1200px;
    height: 702px;
    overflow: hidden;
    background: var(--card-bg);
  }
  .card {
    position: relative;
    width: 1200px;
    height: 702px;
    background: var(--card-bg);
    overflow: hidden;
  }
  .mascot-art {
    position: absolute;
    left: 0;
    top: 18px;
    width: 520px;
    height: 672px;
    background:
      radial-gradient(ellipse 52% 50% at 42% 48%, var(--tooth-white) 0%, var(--tooth-blue) 55%, transparent 72%),
      radial-gradient(ellipse 60% 58% at 50% 50%, var(--star-green) 0%, var(--star-green) 55%, transparent 75%);
  }
  .practice-name {
    position: absolute;
    right: 50px;
    top: 40px;
    margin: 0;
    font-family: "Tinos", "Times New Roman", serif;
    font-weight: 400;
    font-variant: small-caps;
    font-size: 50px;
    letter-spacing: 1px;
    color: var(--brand-green);
    white-space: nowrap;
  }
  .dentist-name {
    position: absolute;
    right: 50px;
    top: 250px;
    margin: 0;
    font-family: "Didact Gothic", "Century Gothic", sans-serif;
    font-weight: 400;
    font-size: 94px;
    line-height: 1;
    color: var(--sky-blue);
    white-space: nowrap;
  }
  .dentist-degree {
    position: absolute;
    left: 830px;
    top: 382px;
    transform: translateX(-50%);
    margin: 0;
    font-family: "Didact Gothic", "Century Gothic", sans-serif;
    font-size: 53px;
    line-height: 1;
    color: var(--sky-blue);
  }
  .contact {
    position: absolute;
    top: 666px;
    margin: 0;
    font-family: "Didact Gothic", "Century Gothic", sans-serif;
    font-size: 22px;
    line-height: 1;
    color: var(--sky-blue);
    white-space: nowrap;
  }
  .contact-address { left: 225px; }
  .contact-phone { left: 907px; }
  .contact-label { color: var(--label-green); }
</style>
</head>
<body>
  <main class="card">
    <div class="mascot-art" role="img" aria-label="Cartoon smiling tooth mascot standing in front of a bright green star"></div>

    <h1 class="practice-name">Tidewell Pediatric Dentistry</h1>

    <p class="dentist-name">Marcus Hollin</p>
    <p class="dentist-degree">DDS</p>

    <p class="contact contact-address"><span class="contact-label">Address : </span>438 E. Corvell Lane, Austin TX - 78731</p>
    <p class="contact contact-phone"><span class="contact-label">Phone : </span>(512) 284 9153</p>
  </main>
</body>
</html>
```